TropicVoyagez

I need a website similar to http://crestvantale.example. I have the following broad requirements
1. Site should be a itinerary based singapore travel and holiday site. You can visit trevimo.example for domain knowledge but not for design. Design should be exact replica of crestvantale.example
2. Site should be same as http://crestvantale.example. Links placement, Logo Placement, Forms design, scrolling, THE MAIN VIDEO LIKE GIF (required and acceptance reqd.), fonts, social links, javascript(copy not reinvent) et al. Please ask as many questions if you have queries. This is very important. I am a CS Grad so won't accept deviation because i know web programming. Design should be exact replica
3. Please use images from Creative Commons travel images from pixlane or internet especially singapore popular destinations. images will help my sale and please ensure creative quality.
4. Cross Browser importantly IE versions because target customers may be computer illiterates
5. HTML5/css3 and follow latest Standards and practices.
6. Clean Commented HTML and css code for maintainability.

Hoping for the world's best creative and experienced professional who have done similar designs to accept my project.

Industry/Entity Type

Internet

```html
<!DOCTYPE html>
<html lang="en">
<head>
<meta charset="utf-8">
<title>TropicVoyagez</title>
<link rel="stylesheet" href="https://fonts.googleapis.com/css2?family=Arimo:wght@400;700&family=Open+Sans:wght@400;600&display=swap">
<style>
:root{
  --red:#e0452d;
  --ink:#333333;
  --muted:#666666;
  --contact:#333333;
  --footer:#262626;
  --slate:#3f5365;
}
*{box-sizing:border-box;margin:0;padding:0}
html,body{width:1200px;height:3066px;overflow:hidden;background:#fff}
body{position:relative;font-family:"Arimo",Arial,sans-serif;color:var(--ink)}
.abs{position:absolute}
.center{text-align:center;left:0;width:1200px}

/* header */
.site-header{position:absolute;top:0;left:0;width:1200px;height:78px;background:#fff}
.brand{left:172px;top:22px;font-size:27px;font-weight:700;color:var(--red);letter-spacing:-.3px}
.nav a{position:absolute;top:31px;font-size:12px;color:var(--ink);text-decoration:none}
.login-btn{left:945px;top:24px;width:82px;height:30px;background:var(--red);color:#fff;font-size:11px;line-height:30px;text-align:center;border-radius:2px}

/* hero */
.hero{top:78px;left:0;width:1200px;height:450px;overflow:hidden;
  background:
    radial-gradient(ellipse 260px 230px at 520px 300px, rgba(150,40,35,.55), rgba(150,40,35,0) 70%),
    radial-gradient(ellipse 520px 230px at 160px 420px, rgba(60,50,40,.95), rgba(60,50,40,0) 75%),
    radial-gradient(ellipse 700px 260px at 900px 200px, rgba(40,80,80,.6), rgba(40,80,80,0) 80%),
    linear-gradient(180deg,#8a8066 0%,#9a8c70 5%,#6e6a58 9%,#4d5d58 16%,#3f5652 40%,#3a4c48 70%,#2d3a36 100%)}
.hero-shade{left:0;top:0;width:1200px;height:450px;background:linear-gradient(90deg,rgba(0,0,0,0) 50%,rgba(0,0,0,.18) 100%)}
.hero-title{left:683px;top:112px;color:#fff;font-size:32px;line-height:1.35;font-weight:400}
.hero-title span{font-size:46px}
.hero-input{left:690px;top:224px;width:340px;height:38px;background:#fff;border-radius:2px;font-size:11px;color:#999;padding:12px 18px}
.hero-btn{left:690px;top:275px;width:185px;height:37px;background:var(--red);color:#fff;font-size:11px;line-height:37px;text-align:center;border-radius:2px}
.hero-hint{left:690px;top:330px;color:#fff;font-size:11px}
.hero-arrow{left:1100px;top:195px}

/* section titles */
.section-title{font-size:21px;color:var(--red);font-weight:400;letter-spacing:.3px}
.section-lead{font-size:11.5px;color:var(--muted);line-height:25px}

/* how it works */
.step{width:300px;text-align:center}
.step h3{font-size:16px;color:var(--red);font-weight:400;margin-top:22px}
.step p{font-size:10.5px;line-height:22px;color:var(--muted);width:230px;margin:14px auto 0}
.step svg{display:block;margin:0 auto}

/* destinations band */
.band{top:1025px;left:0;width:1200px;height:407px;background:var(--red)}
.band-title{top:50px;font-size:22px;color:#fff;font-weight:400}
.dest{width:164px;text-align:center;color:#fff}
.dest .ph{height:164px;width:164px}
.dest b{display:block;font-size:10.5px;margin-top:18px}
.dest small{display:block;font-size:9.5px;line-height:19px;margin-top:2px}

/* partners */
.partner{font-size:28px;font-weight:700;color:#1f2b4a}

/* tweet band */
.tweet{top:1652px;left:0;width:1200px;height:378px;
  background:
    radial-gradient(ellipse 420px 200px at 600px 190px, rgba(58,77,94,.85), rgba(58,77,94,0) 80%),
    linear-gradient(90deg,#56687a,#45596b 30%,#4b5e70 70%,#56687a)}
.tweet p{font-family:"Open Sans",Arial,sans-serif;color:#fff;font-size:15px;line-height:23px}
.tweet .meta{font-family:"Open Sans",Arial,sans-serif;color:#fff;font-size:14px}
.tweet .meta span{color:#c5ced6;font-size:12px}
.dot{width:9px;height:9px;border-radius:50%;background:#7b8b9a}

/* testimonials */
.person{width:222px;text-align:center}
.person .ph{width:222px;height:208px}
.person b{display:block;font-weight:400;color:var(--red);font-size:14px;margin-top:18px}
.person small{display:block;font-size:11px;color:var(--muted);margin-top:6px}

/* subscribe */
.subscribe{top:2548px;left:0;width:1200px;height:76px;background:var(--red)}
.subscribe .lbl{left:172px;top:29px;color:#fff;font-size:14px}
.subscribe .field{left:523px;top:22px;width:322px;height:33px;background:#fff;font-size:10px;color:#777;padding:11px 14px;border-radius:2px}
.subscribe .go{left:858px;top:22px;width:169px;height:33px;background:#5d6670;color:#fff;font-size:10px;font-weight:700;line-height:33px;text-align:center;border-radius:2px}

/* contact */
.contact{top:2624px;left:0;width:1200px;height:374px;background:var(--contact);color:#fff}
.contact h2{font-weight:400;font-size:23px}
.contact .lead{font-size:12px}
.col h4{color:var(--red);font-size:13px;font-weight:700}
.col p{font-size:11px;line-height:21px;margin-top:12px}

/* footer */
.site-footer{top:2998px;left:0;width:1200px;height:68px;background:var(--footer)}
.copy{left:172px;top:28px;color:#ccc;font-size:11px}
.social{top:20px;width:28px;height:28px;border-radius:50%;background:#6a6a6a}
</style>
</head>
<body>

<header class="site-header">
  <div class="abs brand">TropicVoyagez</div>
  <nav class="nav">
    <a style="left:643px">Home</a>
    <a style="left:741px">About us</a>
    <a style="left:853px">Contact us</a>
  </nav>
  <div class="abs login-btn">LOGIN &#9662;</div>
</header>

<section class="abs hero" role="img" aria-label="Traveller in a red cap sitting on harbour rocks looking out over a bay full of boats, with a waterfront town along the far shore">
  <div class="abs hero-shade"></div>
  <h1 class="abs hero-title">Create custom trips in<br><span>15 minutes</span></h1>
  <div class="abs hero-input">Where are you going?</div>
  <div class="abs hero-btn">GET STARTED</div>
  <div class="abs hero-hint">Not sure? Try one of these - Paris,Italy,China</div>
  <svg class="abs hero-arrow" width="14" height="70" viewBox="0 0 14 70"><path d="M2 2 L12 35 L2 68" fill="none" stroke="#ffffff" stroke-opacity=".5" stroke-width="1.5"/></svg>
</section>

<h2 class="abs center section-title" style="top:597px">HOW IT WORKS</h2>
<p class="abs center section-lead" style="top:643px">Lorem Ipsum is simply dummy text of the printing and typesetting industry. Lorem Ipsum has been the industry's<br>standard dummy text ever since the 1500s, when an unknown printer...</p>

<div class="abs step" style="left:137px;top:735px">
  <svg width="90" height="100" viewBox="0 0 90 100"><circle cx="52" cy="10" r="8" fill="#333"/><path d="M44 22 h16 l6 30 -6 2 -2 36 h-7 l-1-26 -3 26 h-7 l2-40 z" fill="#333"/><rect x="14" y="56" width="36" height="26" rx="4" fill="#333"/><path d="M18 56 v-10 h10" fill="none" stroke="#333" stroke-width="3"/><circle cx="20" cy="87" r="4" fill="#333"/><circle cx="44" cy="87" r="4" fill="#333"/></svg>
  <h3>CHOOSE TRIP</h3>
  <p>Lorem Ipsum is simply dummy text of the printing and typesetting industry. Lorem Ipsum has been the industry's...</p>
</div>
<div class="abs step" style="left:455px;top:735px">
  <svg width="90" height="100" viewBox="0 0 90 100"><path d="M34 20 a16 16 0 1 0 0.1 0 Z M34 28 a8 8 0 1 1 -0.1 0 Z" fill="#333" fill-rule="evenodd"/><path d="M22 50 L34 72 L46 50" fill="#333"/><path d="M34 72 Q40 92 62 80 Q78 70 70 50" fill="none" stroke="#333" stroke-width="3"/><circle cx="70" cy="40" r="11" fill="none" stroke="#333" stroke-width="4"/></svg>
  <h3>CUSTOMIZE AND PLAN</h3>
  <p>Lorem Ipsum is simply dummy text of the printing and typesetting industry. Lorem Ipsum has been the industry's...</p>
</div>
<div class="abs step" style="left:770px;top:735px">
  <svg width="90" height="100" viewBox="0 0 90 100"><g transform="rotate(-40 45 55)"><rect x="10" y="50" width="72" height="10" rx="5" fill="#333"/><path d="M40 52 L28 22 L38 22 L58 52 Z M40 58 L28 88 L38 88 L58 58 Z M14 52 L8 38 L14 38 L22 52 Z M14 58 L8 72 L14 72 L22 58 Z" fill="#333"/></g></svg>
  <h3>BOOK YOUR TRIP</h3>
  <p>Lorem Ipsum is simply dummy text of the printing and typesetting industry. Lorem Ipsum has been the industry's...</p>
</div>

<section class="abs band">
  <h2 class="abs center band-title">Some of 2013's 10,242 attendees from 98 countries around the world</h2>
  <svg class="abs" style="left:174px;top:190px" width="14" height="44" viewBox="0 0 14 44"><path d="M12 2 L2 22 L12 42" fill="none" stroke="#fff" stroke-opacity=".6" stroke-width="1.5"/></svg>
  <svg class="abs" style="left:1012px;top:190px" width="14" height="44" viewBox="0 0 14 44"><path d="M2 2 L12 22 L2 42" fill="none" stroke="#fff" stroke-opacity=".6" stroke-width="1.5"/></svg>
  <div class="abs dest" style="left:223px;top:121px"><div class="ph" role="img" aria-label="Harbour bridge lit up at night over the water" style="background:radial-gradient(ellipse 90px 40px at 60px 70px,rgba(230,220,200,.7),rgba(230,220,200,0)),linear-gradient(180deg,#1d3f7a 0%,#2f5a94 45%,#8a7a5a 70%,#d6a850 82%,#2a3a5a 100%)"></div><b>RAVEL ONKAR</b><small>Voltra, Orbix, Sunfield<br>South Africa</small></div>
  <div class="abs dest" style="left:420px;top:121px"><div class="ph" role="img" aria-label="Waterfront skyline with fireworks at night" style="background:radial-gradient(circle 30px at 130px 40px,rgba(240,200,120,.7),rgba(240,200,120,0)),linear-gradient(180deg,#0d1424 0%,#1c2338 40%,#6a4a3a 62%,#e0a040 72%,#4a2c30 100%)"></div><b>RAVEL ONKAR</b><small>Voltra, Orbix, Sunfield<br>South Africa</small></div>
  <div class="abs dest" style="left:615px;top:121px"><div class="ph" role="img" aria-label="City towers at dusk reflected in a river" style="background:linear-gradient(180deg,#c9a070 0%,#d08858 35%,#c45a3a 60%,#e6b060 70%,#3a2c30 100%)"></div><b>RAVEL ONKAR</b><small>Voltra, Orbix, Sunfield<br>South Africa</small></div>
  <div class="abs dest" style="left:814px;top:121px"><div class="ph" role="img" aria-label="Lit iron tower at night above a park" style="background:radial-gradient(ellipse 24px 70px at 82px 70px,rgba(240,190,90,.8),rgba(240,190,90,0)),linear-gradient(180deg,#0b1428 0%,#1c2848 55%,#24463a 78%,#3a6a3c 100%)"></div><b>RAVEL ONKAR</b><small>Voltra, Orbix, Sunfield<br>South Africa</small></div>
</section>

<h2 class="abs center section-title" style="top:1477px">PREVIOUS ATTENDEES INCLUDE</h2>
<div class="abs partner" style="left:224px;top:1558px;font-size:25px">Marketa</div>
<div class="abs partner" style="left:394px;top:1558px">Paylume</div>
<div class="abs partner" style="left:563px;top:1558px">Vantix</div>
<div class="abs partner" style="left:712px;top:1558px;font-size:24px">Cardiona</div>
<div class="abs partner" style="left:845px;top:1560px;font-size:24px">Findexa</div>

<section class="abs tweet" role="img" aria-label="Faded mosaic of member portraits behind the latest tweet">
  <div class="abs" style="left:581px;top:60px;width:28px;height:28px;border-radius:50%;background:#fff"></div>
  <p class="abs center" style="top:130px">Beautiful Examples of Login Forms for Websites and Apps -<br><u>http://formcraft.example/login/new</u> on Formcraft<br>#inspiration. Share new designs with us!</p>
  <div class="abs center meta" style="top:245px">@pixelNomad <span>6 days ago</span></div>
  <div class="abs dot" style="left:561px;top:303px;background:#fff"></div>
  <div class="abs dot" style="left:587px;top:303px"></div>
  <div class="abs dot" style="left:613px;top:303px"></div>
</section>

<h2 class="abs center section-title" style="top:2089px">TESTIMONIALS</h2>
<p class="abs center section-lead" style="top:2136px">Lorem Ipsum is simply dummy text of the printing and typesetting industry. Lorem Ipsum has been the industry's<br>standard dummy text ever since the 1500s, when an unknown printer...</p>
<svg class="abs" style="left:150px;top:2312px" width="12" height="40" viewBox="0 0 12 40"><path d="M10 2 L2 20 L10 38" fill="none" stroke="#e8b0a6" stroke-width="1.5"/></svg>
<svg class="abs" style="left:1040px;top:2312px" width="12" height="40" viewBox="0 0 12 40"><path d="M2 2 L10 20 L2 38" fill="none" stroke="#e8b0a6" stroke-width="1.5"/></svg>
<div class="abs person" style="left:197px;top:2226px"><div class="ph" role="img" aria-label="Portrait of a smiling man at a laptop" style="background:radial-gradient(ellipse 80px 90px at 110px 90px,rgba(190,130,95,.9),rgba(190,130,95,0)),linear-gradient(180deg,#9cc0d8 0%,#b8ccd8 55%,#e8e8e8 100%)"></div><b>Marlo Quent</b><small>Marketing Executive</small></div>
<div class="abs person" style="left:490px;top:2226px"><div class="ph" role="img" aria-label="Portrait of a smiling traveller in a red cap" style="background:radial-gradient(ellipse 70px 40px at 100px 30px,rgba(200,40,40,.9),rgba(200,40,40,0)),radial-gradient(ellipse 60px 70px at 110px 110px,rgba(220,160,120,.9),rgba(220,160,120,0)),linear-gradient(180deg,#d6c290 0%,#b89a60 50%,#8a3c2c 100%)"></div><b>Marlo Quent</b><small>Marketing Executive</small></div>
<div class="abs person" style="left:781px;top:2226px"><div class="ph" role="img" aria-label="Portrait of a smiling woman with long hair" style="background:radial-gradient(ellipse 70px 90px at 120px 100px,rgba(215,160,120,.85),rgba(215,160,120,0)),radial-gradient(ellipse 120px 130px at 130px 110px,rgba(170,110,60,.7),rgba(170,110,60,0)),linear-gradient(180deg,#e6e2dc,#cfc6bc)"></div><b>Marlo Quent</b><small>Marketing Executive</small></div>

<section class="abs subscribe">
  <div class="abs lbl">Get our recent updates through your email id :</div>
  <div class="abs field">Enter your email id :</div>
  <div class="abs go">SUBSCRIBE</div>
</section>

<section class="abs contact">
  <h2 class="abs center" style="top:60px">CONTACT US</h2>
  <p class="abs center lead" style="top:118px">Lorem Ipsum is simply dummy text of the printing and typesetting industry.</p>
  <svg class="abs" style="left:175px;top:190px" width="34" height="34" viewBox="0 0 24 24"><path d="M6.6 10.8a15 15 0 0 0 6.6 6.6l2.2-2.2a1 1 0 0 1 1-.25 11 11 0 0 0 3.6.6 1 1 0 0 1 1 1V20a1 1 0 0 1-1 1A17 17 0 0 1 3 4a1 1 0 0 1 1-1h3.5a1 1 0 0 1 1 1 11 11 0 0 0 .6 3.6 1 1 0 0 1-.25 1Z" fill="#fff"/></svg>
  <div class="abs col" style="left:237px;top:196px"><h4>PHONES</h4><p>+ ( 1450 ) 330 118<br>+ ( 1450 ) 330 274</p></div>
  <svg class="abs" style="left:462px;top:188px" width="26" height="38" viewBox="0 0 24 36"><path d="M12 0a12 12 0 0 0-12 12c0 9 12 24 12 24s12-15 12-24A12 12 0 0 0 12 0Zm0 17a5 5 0 1 1 0-10 5 5 0 0 1 0 10Z" fill="#fff"/></svg>
  <div class="abs col" style="left:519px;top:196px"><h4>OFFICE ADDRESS</h4><p>120, Streat name,<br>State nname,<br>Country name, Zipcode : 2103200<br>+ ( 1450 ) 330 274</p></div>
  <svg class="abs" style="left:795px;top:192px" width="42" height="30" viewBox="0 0 42 30"><rect x="1" y="1" width="40" height="28" fill="#fff"/><path d="M1 1 L21 17 L41 1" fill="none" stroke="#333" stroke-width="2.5"/></svg>
  <div class="abs col" style="left:862px;top:196px"><h4>EMAILS</h4><p>office@tropicvoyagez.example<br>sales@tropicvoyagez.example</p></div>
</section>

<footer class="abs site-footer">
  <div class="abs copy">Copyright 2014. TropicVoyagez. All rights reserved.</div>
  <div class="abs social" style="left:815px"></div>
  <div class="abs social" style="left:851px"></div>
  <div class="abs social" style="left:887px"></div>
  <div class="abs social" style="left:923px"></div>
  <div class="abs social" style="left:959px"></div>
  <div class="abs social" style="left:995px"></div>
</footer>

</body>
</html>
```